Webshop facelift - modern, sales oriented, mobile first

We need facelifted webshop, which is running for few years.
www.kolvarna.si
Some of the basic requirements:

1.) Logo must basicly stay the same, it could only be a little "modernised".
2.) Main goal is to generate more sales, so webpage must be much more sales oriented.
3.) Focus is on category page and product page. Those two page types must be realy designed very well
4.) Mobile first, there are 80% customers over mobile devices
5.) Mobile menu must be also much better
6.) Category description will go under listed products
7.) On product page, there must be much bigger product images, and also mobile friendly image slider
8.) Big add to cart buttons
9.) Badges about safe shopping, possible returning goods, 100% warranty
10.) exposed product videos, images between text
11.) cleary exposed product benefits
11.) Products, which have sizes to choose, must have more user friendly choose option
12.) category page on desktop can have only products in all width, not side menu on the left
13.) Exposed CTA's on product page

You can create this category page: https://kolvarna.si/posteljnina
You can create this product page: https://kolvarna.si/oblikovalni-pas-brinel-hlacke

In short: mobile first, very sales oriented, look like 2018, big images, great shopping experience.

Target Market(s)

6 European coutries

Industry/Entity Type

E-Commerce

Number of Pages Required

3 page

Font styles to use
Sans Serif

Colors

Designer to choose colors to be used in the design.

Requirements
Must have
• Mobile first design
• Big images
• Very sales oriented
• CTA's through product description
Nice to have
• Product badges, like for example "100% cotton", "On stock", "Sale", "New"
Should not have
• Should not be copied from somewhere.

```html
<!DOCTYPE html>
<html lang="sl">
<head>
<meta charset="utf-8">
<title>Kolvarna – spletna trgovina</title>
<link rel="stylesheet" href="https://fonts.googleapis.com/css2?family=Poppins:wght@400;500;600;700&display=swap">
<style>
  :root {
    --accent: #f6b800;
    --accent-dark: #d99f00;
    --ink: #222428;
    --muted: #8a8d93;
    --line: #e6e6e6;
    --hero-top: #3a3b3e;
    --hero-bottom: #1d1e20;
    --blue: #2e6fb3;
    --paper: #ffffff;
    --soft: #f5f5f5;
  }
  * { box-sizing: border-box; margin: 0; padding: 0; }
  html, body { width: 1200px; height: 600px; overflow: hidden; }
  body { font-family: "Poppins", Arial, sans-serif; color: var(--ink); background: var(--paper); position: relative; }

  .site-header {
    position: absolute; top: 0; left: 0; width: 1200px; height: 56px; z-index: 3;
    display: flex; align-items: center; justify-content: center; gap: 40px;
    background: rgba(20, 20, 22, .35);
  }
  .brand { display: flex; align-items: center; gap: 8px; color: #fff; font-weight: 700; font-size: 17px; letter-spacing: .5px; }
  .brand-dot { width: 14px; height: 14px; border-radius: 50%; background: var(--accent); }
  .main-nav { display: flex; gap: 18px; list-style: none; }
  .main-nav li { color: #fff; font-size: 10.5px; font-weight: 500; text-transform: uppercase; letter-spacing: .4px; }
  .header-tools { display: flex; gap: 14px; }

  .hero {
    position: absolute; top: 0; left: 0; width: 1200px; height: 340px;
    background: linear-gradient(180deg, var(--hero-top), var(--hero-bottom));
  }
  .hero-visual {
    position: absolute; left: 150px; top: 40px; width: 880px; height: 280px;
    background: radial-gradient(ellipse at 45% 50%, #6a6c70 0%, #3a3b3e 55%, transparent 75%);
  }
  .hero-copy { position: absolute; left: 0; width: 1200px; top: 160px; text-align: center; color: #fff; z-index: 2; }
  .hero-title { font-size: 34px; font-weight: 700; letter-spacing: 1px; }
  .hero-sub { font-size: 12px; margin-top: 6px; opacity: .85; }
  .btn-shop {
    display: inline-block; margin-top: 14px; background: var(--accent); color: #fff;
    font-size: 10px; font-weight: 600; padding: 8px 18px; letter-spacing: .6px; text-transform: uppercase;
  }
  .slider-arrow {
    position: absolute; top: 180px; width: 24px; height: 24px; display: flex; align-items: center; justify-content: center; z-index: 2;
  }
  .slider-arrow.prev { left: 70px; background: rgba(255,255,255,.15); }
  .slider-arrow.next { right: 70px; background: var(--accent); }

  .promo {
    position: absolute; left: 60px; top: 290px; width: 320px; height: 290px; z-index: 2;
  }
  .promo-frame { position: absolute; left: 0; top: 70px; width: 90px; height: 90px; border-left: 3px solid var(--accent); border-top: 3px solid var(--accent); }
  .promo-card {
    position: absolute; left: 40px; top: 0; width: 240px; height: 250px; background: var(--paper);
    box-shadow: 0 8px 30px rgba(0,0,0,.12); text-align: center; padding-top: 62px;
  }
  .promo-card .corner { position: absolute; width: 16px; height: 16px; border-color: var(--accent); border-style: solid; }
  .corner.tl { left: 14px; top: 14px; border-width: 2px 0 0 2px; }
  .corner.br { right: 14px; bottom: 14px; border-width: 0 2px 2px 0; }
  .promo-title { font-size: 15px; font-weight: 700; text-transform: uppercase; letter-spacing: .5px; }
  .promo-price { font-size: 18px; color: var(--blue); font-weight: 600; margin-top: 12px; }
  .promo-note { font-size: 10px; color: var(--muted); margin-top: 4px; }
  .promo-card .btn-shop { margin-top: 18px; }

  .featured { position: absolute; left: 420px; top: 356px; width: 740px; }
  .section-title { text-align: center; font-size: 15px; font-weight: 700; color: var(--blue); text-transform: uppercase; letter-spacing: .6px; }
  .section-rule { width: 30px; height: 3px; background: var(--accent); margin: 6px auto 0; }
  .tabs { display: flex; justify-content: center; gap: 16px; list-style: none; margin-top: 12px; font-size: 10px; color: var(--muted); }
  .tabs li.active { background: var(--accent); color: #fff; padding: 1px 10px; border-radius: 8px; }
  .product-grid { display: flex; gap: 20px; margin-top: 14px; }
  .product-card { width: 170px; text-align: center; }
  .product-media { width: 170px; height: 110px; position: relative; }
  .badge-partner { position: absolute; right: 8px; top: 8px; width: 22px; height: 22px; border-radius: 50%; background: var(--blue); }
  .product-name { font-size: 10px; margin-top: 8px; }
  .product-price { font-size: 11px; margin-top: 3px; }
  .product-price .now { color: var(--blue); font-weight: 600; }
  .product-price .was { color: var(--muted); text-decoration: line-through; margin-left: 5px; }
  .rating { display: flex; justify-content: center; gap: 2px; margin-top: 3px; }
  .rating span { width: 7px; height: 7px; background: var(--accent); clip-path: polygon(50% 0,61% 35%,98% 35%,68% 57%,79% 91%,50% 70%,21% 91%,32% 57%,2% 35%,39% 35%); }
</style>
</head>
<body>
  <section class="hero">
    <div class="hero-visual" role="img" aria-label="Three smartphones lying at an angle on a dark surface"></div>
  </section>

  <header class="site-header">
    <div class="brand"><span class="brand-dot"></span>KOLVARNA</div>
    <ul class="main-nav">
      <li>Dom in bivanje</li><li>Posteljnina</li><li>Otroci</li><li>Lepota</li><li>Zdravje</li><li>Hobi</li><li>Praznik &amp; party</li>
    </ul>
    <div class="header-tools">
      <svg width="12" height="12" viewBox="0 0 12 12"><circle cx="5" cy="5" r="3.8" fill="none" stroke="#fff" stroke-width="1.4"/><line x1="8" y1="8" x2="11" y2="11" stroke="#fff" stroke-width="1.4"/></svg>
      <svg width="13" height="12" viewBox="0 0 13 12"><path d="M0 1h2.5l1.8 7h6.5l1.5-5H3.4" fill="none" stroke="#fff" stroke-width="1.3"/><circle cx="5" cy="10.5" r="1" fill="#fff"/><circle cx="10" cy="10.5" r="1" fill="#fff"/></svg>
    </div>
  </header>

  <div class="hero-copy">
    <h1 class="hero-title">MAKES YOUR LIFE PERFECT</h1>
    <p class="hero-sub">Everything you need to get started with Kolvarna</p>
    <span class="btn-shop">Shop now</span>
  </div>
  <div class="slider-arrow prev"><svg width="8" height="10" viewBox="0 0 8 10"><path d="M6 1 2 5l4 4" fill="none" stroke="#fff" stroke-width="1.6"/></svg></div>
  <div class="slider-arrow next"><svg width="8" height="10" viewBox="0 0 8 10"><path d="M2 1l4 4-4 4" fill="none" stroke="#fff" stroke-width="1.6"/></svg></div>

  <aside class="promo">
    <div class="promo-frame"></div>
    <div class="promo-card">
      <span class="corner tl"></span><span class="corner br"></span>
      <h2 class="promo-title">Lattest mobile</h2>
      <p class="promo-price">from $300</p>
      <p class="promo-note">fine titanium finish</p>
      <span class="btn-shop">Shop now</span>
    </div>
  </aside>

  <section class="featured">
    <h2 class="section-title">Featured products</h2>
    <div class="section-rule"></div>
    <ul class="tabs"><li class="active">All</li><li>Digital</li><li>Baby</li><li>Workout</li><li>Clothes</li><li>Accessories</li></ul>
    <div class="product-grid">
      <article class="product-card">
        <div class="product-media" role="img" aria-label="Blue waist trimmer belt" style="background:linear-gradient(135deg,#d9c2ad,#3c64a8)"></div>
        <p class="product-name">Sports waist zipper trimmer</p>
        <p class="product-price"><span class="now">$35.00</span><span class="was">$42.00</span></p>
        <div class="rating"><span></span><span></span><span></span><span></span><span></span></div>
      </article>
      <article class="product-card">
        <div class="product-media" role="img" aria-label="Fitness shaping product in use" style="background:linear-gradient(135deg,#f1d3bf,#e86f8a)"></div>
        <p class="product-name">Shaping hip lift trainer set</p>
        <p class="product-price"><span class="now">$18.00</span><span class="was">$24.00</span></p>
        <div class="rating"><span></span><span></span><span></span><span></span><span></span></div>
      </article>
      <article class="product-card">
        <div class="product-media" role="img" aria-label="Set of small white speakers" style="background:linear-gradient(135deg,#f4f4f4,#c9cdd2)"></div>
        <p class="product-name">Mini wireless speaker duo</p>
        <p class="product-price"><span class="now">$36.00</span><span class="was">$40.00</span></p>
        <div class="rating"><span></span><span></span><span></span><span></span><span></span></div>
      </article>
      <article class="product-card">
        <div class="product-media" role="img" aria-label="Grey luggage travel set" style="background:linear-gradient(135deg,#eef0f2,#4b5560)"><span class="badge-partner"></span></div>
        <p class="product-name">Travel luggage set of three</p>
        <p class="product-price"><span class="now">$140.00</span><span class="was">$178.00</span></p>
        <div class="rating"><span></span><span></span><span></span><span></span><span></span></div>
      </article>
    </div>
  </section>
</body>
</html>
```